New web design for a service provider in the medical field

We are looking for a new design for our website. We are a company that repairs and sells medical endoscopes. Our customers include doctors and hospitals. Our current website can be found at https://lumenfix.example/en/lumenfix-english.
We need a new web design (without programming) for the following 3 pages:
-Startpage https://lumenfix.example/en/lumenfix-english/
-Used endoscopes https://lumenfix.example/en/used-endoscopes/
-Purchase https://lumenfix.example/en/purchase/
The design should be modern and stylish.
The blue color of the logo should be reflected on the page, but not too intrusive.
I have uploaded the images from the header. If more images are needed, let me know and I will upload them.

Target Market(s)
Doctors and hospitals

```html
<!DOCTYPE html>
<html lang="en">
<head>
<meta charset="utf-8">
<title>LumenFix – Endoscope Repair</title>
<link rel="stylesheet" href="https://fonts.googleapis.com/css2?family=Source+Sans+3:wght@400;600;700&display=swap">
<style>
  :root {
    --brand-blue: #1f9ad6;
    --brand-blue-deep: #0b78d8;
    --ink: #24384a;
    --nav-ink: #2f3a44;
    --rule: #e6e9ec;
    --white: #ffffff;
    --photo-dark: #1d3042;
    --photo-mid: #6d7c8a;
    --photo-light: #d3d7db;
  }
  * { box-sizing: border-box; margin: 0; padding: 0; }
  html, body { width: 1200px; height: 838px; overflow: hidden; background: var(--white); }
  body { font-family: "Source Sans 3", "Myriad Pro", Arial, sans-serif; color: var(--ink); position: relative; }

  .hero-shapes { position: absolute; left: 0; top: 0; width: 1200px; height: 838px; }

  .site-header { position: absolute; left: 0; top: 0; width: 1200px; height: 64px; border-bottom: 1px solid var(--rule); background: var(--white); }
  .brand { position: absolute; left: 170px; top: 40px; display: flex; align-items: center; gap: 8px; }
  .brand-dot { width: 14px; height: 14px; border-radius: 50%; background: var(--brand-blue); }
  .brand-name { font-size: 26px; font-weight: 700; color: #1f3a57; letter-spacing: .2px; }

  .contact { position: absolute; top: 13px; display: flex; gap: 12px; }
  .contact-email { left: 478px; }
  .contact-phone { left: 672px; }
  .contact-label { font-size: 13px; font-weight: 600; color: var(--brand-blue); letter-spacing: .3px; }
  .contact-value { font-size: 13px; color: var(--nav-ink); margin-top: 2px; }
  .contact svg { margin-top: 6px; }

  .appointment-btn { position: absolute; left: 852px; top: 11px; width: 179px; height: 39px; border: 1.5px solid var(--brand-blue); border-radius: 20px; color: var(--brand-blue); font-size: 13px; font-weight: 600; letter-spacing: .4px; display: flex; align-items: center; justify-content: center; text-decoration: none; }

  .main-nav { position: absolute; top: 77px; left: 367px; display: flex; gap: 0; font-size: 12px; color: var(--nav-ink); }
  .main-nav a { color: inherit; text-decoration: none; position: absolute; white-space: nowrap; }

  .photo-area { position: absolute; left: 0; top: 0; }

  .hero-copy { position: absolute; left: 167px; top: 256px; color: var(--white); }
  .hero-kicker { font-size: 32px; font-weight: 700; letter-spacing: -.2px; line-height: 1; }
  .hero-title { font-size: 88px; font-weight: 700; line-height: 96px; margin-top: 14px; letter-spacing: -.5px; }

  .get-in-touch { position: absolute; right: 168px; top: 662px; font-size: 22px; font-weight: 600; color: var(--ink); }
  .social-list { position: absolute; left: 862px; top: 701px; display: flex; gap: 9px; list-style: none; }
  .social-list li { width: 36px; height: 36px; border-radius: 50%; border: 1.5px solid var(--brand-blue); }
  .social-list li.is-active { background: var(--brand-blue); }
</style>
</head>
<body>

<svg class="hero-shapes" viewBox="0 0 1200 838" aria-hidden="true">
  <defs>
    <linearGradient id="photoTone" x1="0" y1="0" x2="1" y2="0.6">
      <stop offset="0" stop-color="var(--photo-dark)"/>
      <stop offset="0.45" stop-color="#4b5b6b"/>
      <stop offset="0.8" stop-color="#a9b2ba"/>
      <stop offset="1" stop-color="var(--photo-light)"/>
    </linearGradient>
    <linearGradient id="blueTone" x1="0" y1="0" x2="0.4" y2="1">
      <stop offset="0" stop-color="#0a6fe0"/>
      <stop offset="0.6" stop-color="#0e8ff0"/>
      <stop offset="1" stop-color="#18b0f4"/>
    </linearGradient>
  </defs>
  <g role="img" aria-label="Photo of a flexible endoscope with its control body lying on a light surface">
    <path d="M0 100 C120 140 230 190 360 182 L1200 100 L1200 468 L720 708 Q690 724 660 710 L0 490 Z" fill="url(#photoTone)"/>
  </g>
  <g role="img" aria-label="Blue panel with a soft medical cross texture">
    <path d="M0 492 L528 665 L300 782 Q272 796 240 786 L0 700 Z" fill="url(#blueTone)"/>
  </g>
  <line x1="1085" y1="300" x2="1085" y2="318" stroke="#fff" stroke-width="1.5"/>
  <line x1="1085" y1="338" x2="1085" y2="356" stroke="#fff" stroke-width="1.5"/>
  <circle cx="1085" cy="282" r="19" fill="#2aa2e0" stroke="#fff" stroke-width="1.5"/>
  <path d="M1085 292 V273 M1080 278 L1085 272 L1090 278" stroke="#fff" stroke-width="2" fill="none"/>
  <circle cx="1085" cy="378" r="24" fill="#1a7fb8" stroke="#fff" stroke-width="1.5"/>
  <path d="M1085 366 V389 M1079 383 L1085 390 L1091 383" stroke="#fff" stroke-width="2" fill="none"/>
</svg>

<header class="site-header">
  <div class="brand">
    <span class="brand-dot"></span>
    <span class="brand-name">LumenFix</span>
  </div>

  <div class="contact contact-email">
    <svg width="28" height="20" viewBox="0 0 28 20"><rect x="1" y="1" width="26" height="18" rx="1" fill="none" stroke="var(--brand-blue)" stroke-width="1.6"/><path d="M1 2 L14 12 L27 2" fill="none" stroke="var(--brand-blue)" stroke-width="1.6"/></svg>
    <div>
      <div class="contact-label">EMAIL</div>
      <div class="contact-value">info@lumenfix.example</div>
    </div>
  </div>

  <div class="contact contact-phone">
    <svg width="28" height="28" viewBox="0 0 28 28"><path d="M6 3 L10 3 L12 9 L9 11 Q11 17 17 19 L19 16 L25 18 L25 22 Q25 25 21 25 Q5 23 3 7 Q3 3 6 3 Z" fill="none" stroke="var(--brand-blue)" stroke-width="1.6"/><path d="M16 3 Q24 4 25 12 M16 7 Q21 8 21 12" fill="none" stroke="var(--brand-blue)" stroke-width="1.4"/></svg>
    <div>
      <div class="contact-label">MAKE A CALL</div>
      <div class="contact-value">49 4000 555 210-0</div>
    </div>
  </div>

  <a class="appointment-btn" href="#">MAKE AN APPOINTMENT</a>
</header>

<nav class="main-nav">
  <a href="#" style="left:0">Home</a>
  <a href="#" style="left:71px">Endoscope Repair</a>
  <a href="#" style="left:201px">Used Endoscopes</a>
  <a href="#" style="left:328px">Endoscopy Systems</a>
  <a href="#" style="left:466px">Endoscopy Accessories</a>
  <a href="#" style="left:620px">Purshase</a>
</nav>

<section class="hero-copy">
  <p class="hero-kicker">PUT YOUR ENDOSCOPE</p>
  <h1 class="hero-title">IN RELIABLE<br>HANDS!</h1>
</section>

<p class="get-in-touch">Get In Touch</p>
<ul class="social-list" aria-label="Social channels">
  <li></li>
  <li class="is-active"></li>
  <li></li>
  <li></li>
</ul>

</body>
</html>
```